Corvanta Business cards template

We're looking for something modern and elegant. We are a reseller of technology (computers, datacenter, etc). Color theme would be "only" white with the incorporation of the blue that's present on our website (Corvanta.com) and logo file. We would like for the card to provide all the necessary info for the specific person (Phone#, fax#, email, name, website URL) . I'm attaching the logo file to this request. Please have it show Montreal/New York somewhere, without providing specific addresses.

Target Market(s)

All b2b

Industry/Entity Type

Business

Contact Information for Business Card

Please have the color scheme be represented by only the white and blue from our website (Corvanta.com) and logo. We would like to logo on the card, but not big and overwhelming. This card will be used as a template for anybody within the company, it should display the user's name, phone#, fax#, email, job title and website URL. Please have it show Montreal/New York somewhere, without providing our specific addresses. Really, we're looking for a clean, simple and elegant look.

Font styles to use
Serif

Requirements
Must have
• Please see card details
Nice to have
• Please see card details
Should not have
• Anything tacky or tagline.

```html
<!DOCTYPE html>
<html lang="en">
<head>
<meta charset="utf-8">
<title>Corvanta Business Cards</title>
<link rel="stylesheet" href="https://fonts.googleapis.com/css2?family=Lora:wght@400;700&display=swap">
<style>
  :root {
    --stage: #222222;
    --brand-blue: #0a87cd;
    --brand-blue-light: #0d93d8;
    --brand-blue-deep: #0075c0;
    --paper: #ffffff;
    --ink: #1a1a1a;
  }
  * { box-sizing: border-box; margin: 0; padding: 0; }
  html, body {
    width: 1189px;
    height: 1200px;
    overflow: hidden;
    background: var(--stage);
    font-family: "Lora", Georgia, serif;
  }
  .canvas { position: relative; width: 1189px; height: 1200px; }
  .card {
    position: absolute;
    left: 171px;
    width: 856px;
    height: 488px;
    border-radius: 22px;
    overflow: hidden;
  }
  .card--front {
    top: 67px;
    background: radial-gradient(ellipse at 45% 40%, var(--brand-blue-light) 0%, var(--brand-blue) 55%, var(--brand-blue-deep) 100%);
  }
  .card--back { top: 625px; background: var(--paper); }

  .brand-name {
    position: absolute;
    font-weight: 700;
    white-space: nowrap;
    line-height: 1;
  }
  .card--front .brand-name {
    left: 0; right: 0;
    top: 196px;
    text-align: center;
    font-size: 80px;
    letter-spacing: 5px;
    color: var(--paper);
  }
  .website {
    position: absolute;
    left: 0; right: 0;
    top: 378px;
    text-align: center;
    font-size: 24px;
    line-height: 1.2;
    color: var(--ink);
  }
  .locations {
    position: absolute;
    left: 0; right: 0;
    top: 414px;
    text-align: center;
    font-size: 16px;
    letter-spacing: 3px;
    text-transform: uppercase;
    color: var(--paper);
  }
  .card--back .brand-name {
    left: 58px;
    top: 232px;
    font-size: 54px;
    letter-spacing: 2px;
    color: var(--brand-blue);
  }
  .divider {
    position: absolute;
    left: 427px;
    top: 162px;
    width: 1px;
    height: 191px;
    background: var(--ink);
  }
  .person { position: absolute; left: 474px; top: 165px; }
  .person__name {
    font-size: 29px;
    font-weight: 700;
    color: var(--brand-blue);
    line-height: 1;
    letter-spacing: 0.5px;
  }
  .person__title {
    font-size: 23px;
    color: var(--ink);
    line-height: 1;
    margin-top: 3px;
  }
  .contacts {
    position: absolute;
    left: 474px;
    top: 260px;
    list-style: none;
  }
  .contacts__item {
    display: flex;
    align-items: center;
    height: 31px;
    font-size: 24px;
    color: var(--ink);
  }
  .contacts__icon {
    width: 25px;
    height: 25px;
    margin-right: 7px;
    flex: none;
  }
</style>
</head>
<body>
<main class="canvas">
  <section class="card card--front" aria-label="Business card front">
    <div class="brand-name">Corvanta</div>
    <div class="website">www.yourcompany.com</div>
    <div class="locations">Montreal · New York</div>
  </section>

  <section class="card card--back" aria-label="Business card back">
    <div class="brand-name">Corvanta</div>
    <div class="divider"></div>
    <div class="person">
      <div class="person__name">DANIEL REYES</div>
      <div class="person__title">Managing Partner</div>
    </div>
    <ul class="contacts">
      <li class="contacts__item">
        <svg class="contacts__icon" viewBox="0 0 24 24" aria-label="Phone">
          <rect width="24" height="24" rx="4" fill="var(--brand-blue)"/>
          <path d="M5 10c0-3 14-3 14 0v1.5h-3.5V10h-7v1.5H5z" fill="#fff"/>
          <path d="M8 12h8l2 6H6z" fill="#fff"/>
          <circle cx="12" cy="15" r="1.6" fill="var(--brand-blue)"/>
        </svg>
        (01) 2345 6789
      </li>
      <li class="contacts__item">
        <svg class="contacts__icon" viewBox="0 0 24 24" aria-label="Fax">
          <rect width="24" height="24" rx="4" fill="var(--brand-blue)"/>
          <rect x="7" y="4" width="10" height="6" fill="#fff"/>
          <rect x="4" y="10" width="16" height="7" rx="1.5" fill="#fff"/>
          <rect x="7" y="14" width="10" height="6" fill="#fff" stroke="var(--brand-blue)" stroke-width="1"/>
        </svg>
        (01) 2345 6789
      </li>
      <li class="contacts__item">
        <svg class="contacts__icon" viewBox="0 0 24 24" aria-label="Email">
          <rect width="24" height="24" rx="4" fill="var(--brand-blue)"/>
          <rect x="4" y="6.5" width="16" height="11" fill="#fff"/>
          <path d="M4 6.5l8 6.5 8-6.5M4 17.5l6-5.5M20 17.5l-6-5.5" fill="none" stroke="var(--brand-blue)" stroke-width="1.2"/>
        </svg>
        Info@yourcompany.com
      </li>
    </ul>
  </section>
</main>
</body>
</html>
```